Flier redesign 2021

The 3 prior year fliers are attached. We want a new design for 2021 -

* DO NOT SIMPLY COPY and change the year.
*All text should be the same, except year is 2021.
*Use different photos. You can find photos on our website maplecrestgardens.org or on our google page.

Requirements
Must have
• MUST be done in photoshop an photoshop file must be provided at the end.
Should not have
• Should not be same design as previous years.

```html
<!DOCTYPE html>
<html lang="en">
<head>
<meta charset="utf-8">
<title>Maplecrest Gardens – 2021 Gravesite Landscaping Packages</title>
<link href="https://fonts.googleapis.com/css2?family=Poppins:wght@400;500;600;700;800&display=swap" rel="stylesheet">
<style>
  :root{
    --maroon:#7a1f2e;
    --maroon-dark:#4e1120;
    --panel:#c3c3c3;
    --page:#f2f3f3;
    --ink:#1d1d1d;
    --gold:#f5a623;
    --white:#ffffff;
  }
  *{margin:0;padding:0;box-sizing:border-box}
  html,body{width:848px;height:1200px;overflow:hidden;background:var(--page)}
  body{font-family:"Poppins",sans-serif;color:var(--ink)}
  .flyer{position:relative;width:848px;height:1200px;overflow:hidden;background:var(--page)}

  .header-band{position:absolute;left:0;top:0;width:848px;height:90px;background:var(--white)}
  .brand{position:absolute;left:37px;top:30px;font-size:30px;font-weight:500;color:var(--maroon);letter-spacing:1px}

  .hero-photo{position:absolute;inset:0;
    background:linear-gradient(170deg,#8fb7e2 0%,#9cc0e3 18%,#6f8f4a 45%,#4d6b33 70%,#7a7868 100%);
    clip-path:polygon(0 90px,380px 90px,502px 0,778px 0,300px 352px,264px 423px,0 277px)}
  .accent{position:absolute;inset:0;width:848px;height:1200px}

  .headline{position:absolute;left:522px;top:178px;width:322px;color:var(--white);white-space:nowrap}
  .headline .year{font-size:124px;font-weight:800;line-height:1;letter-spacing:-3px}
  .headline .title{font-size:44px;font-weight:700;line-height:42px;margin-top:-4px;letter-spacing:-.3px}

  .column{position:absolute;top:508px;width:257px;height:467px;background:var(--panel)}
  .col-1{left:33px}.col-2{left:297px}.col-3{left:561px}

  .plan-card{position:absolute;top:471px;width:228px;height:167px;padding:5px;
    background:linear-gradient(90deg,#b07a82,#f0e2e4 50%,#b07a82);box-shadow:0 3px 6px rgba(0,0,0,.3)}
  .plan-card.silver{background:linear-gradient(90deg,#9a9a9a,#f4f4f4 50%,#9a9a9a)}
  .plan-card.gold{background:linear-gradient(90deg,#b8912c,#f1d98a 50%,#b8912c)}
  .card-1{left:48px}.card-2{left:312px}.card-3{left:576px}
  .plan-card .inner{width:100%;height:100%;background:var(--maroon);color:var(--white);text-align:center;position:relative}
  .plan-name{position:absolute;left:0;right:0;top:30px;font-size:21px;font-weight:700;line-height:28px;letter-spacing:.5px}
  .plan-rule{position:absolute;left:19px;right:19px;top:93px;border-top:1px solid rgba(255,255,255,.85)}
  .plan-desc{position:absolute;left:0;right:0;top:104px;font-size:14px;line-height:18px;white-space:nowrap}
  .badge{position:absolute;left:0;right:0;top:10px;font-size:12px;font-weight:700;color:var(--gold);letter-spacing:1.5px}

  .features{position:absolute;top:652px;width:220px;list-style:none}
  .f-1{left:57px}.f-2{left:321px}.f-3{left:585px}
  .features li{position:relative;padding-left:19px;font-size:14.4px;line-height:17px;margin-bottom:17px}
  .features svg{position:absolute;left:0;top:3px;width:12px;height:12px}

  .price-box{position:absolute;top:975px;width:257px;height:128px;background:var(--maroon);color:var(--white);text-align:center}
  .pb-1{left:33px}.pb-2{left:297px}.pb-3{left:561px}
  .terms{position:absolute;left:0;right:0;top:10px;display:flex;justify-content:center}
  .term{width:81px;position:relative}
  .term + .term{border-left:1px solid rgba(255,255,255,.6)}
  .term .label{font-size:14px;line-height:18px;padding-top:2px}
  .term .amount{font-size:27px;font-weight:700;margin-top:10px;line-height:30px;padding-bottom:4px}
  .amount sup,.big-amount sup{font-size:.5em;vertical-align:.7em}
  .pay-label{position:absolute;left:0;right:0;top:12px;font-size:14px}
  .big-amount{position:absolute;left:0;right:0;top:34px;font-size:43px;font-weight:700;line-height:50px}
  .note{position:absolute;left:0;right:0;top:94px;font-size:11px;line-height:13.5px}

  .contact{position:absolute;top:1112px;left:0;width:848px;height:30px;color:var(--maroon);font-size:17px}
  .contact span{position:absolute;top:4px;white-space:nowrap}
  .contact .sep{position:absolute;top:3px;width:1.5px;height:22px;background:var(--maroon)}

  .web-band{position:absolute;left:0;top:1152px;width:848px;height:48px;background:var(--maroon);color:var(--white);text-align:center;font-size:17.5px;line-height:44px;font-weight:500}
</style>
</head>
<body>
<main class="flyer">
  <div class="header-band"></div>
  <div class="brand">MAPLECREST GARDENS</div>

  <div class="hero-photo" role="img" aria-label="Photo of the cemetery office building, a two-storey house with a cupola, surrounded by trees and headstones under a blue sky"></div>

  <svg class="accent" viewBox="0 0 848 1200" aria-hidden="true">
    <defs>
      <linearGradient id="wedge" x1="0" y1="0" x2="1" y2="1">
        <stop offset="0" stop-color="#7a1f2e"/>
        <stop offset="1" stop-color="#4e1120"/>
      </linearGradient>
    </defs>
    <polygon points="778,0 848,0 848,653 308,347" fill="url(#wedge)"/>
    <polyline points="0,292 264,440 352,376" fill="none" stroke="#7a1f2e" stroke-width="11"/>
  </svg>

  <div class="headline">
    <div class="year">2021</div>
    <div class="title">Gravesite<br>Landscaping<br>Packages</div>
  </div>

  <div class="column col-1"></div>
  <div class="column col-2"></div>
  <div class="column col-3"></div>

  <div class="plan-card card-1"><div class="inner">
    <div class="plan-name">SEASONAL<br>CARE</div><div class="plan-rule"></div>
    <div class="plan-desc">Seasonal landscaping<br>grave care</div>
  </div></div>
  <div class="plan-card silver card-2"><div class="inner">
    <div class="plan-name">BASE CARE<br>ENDOWMENT</div><div class="plan-rule"></div>
    <div class="plan-desc">Landscaping care forever for<br>graves with no plantings</div>
  </div></div>
  <div class="plan-card gold card-3"><div class="inner">
    <div class="badge">MOST POPULAR</div>
    <div class="plan-name">PERPETUAL CARE<br>ENDOWMENT</div><div class="plan-rule"></div>
    <div class="plan-desc">Landscaping care forever<br>for graves with plantings</div>
  </div></div>

  <ul class="features f-1">
    <li><svg viewBox="0 0 12 12"><circle cx="6" cy="6" r="6" fill="#7a1f2e"/><path d="M3.2 6.2l2 2 3.6-4" fill="none" stroke="#fff" stroke-width="1.4"/></svg>Wedding and trimming services on your gravesite approximately every 7 weeks during the growing season: mid-April through mid-October</li>
  </ul>
  <ul class="features f-2">
    <li><svg viewBox="0 0 12 12"><circle cx="6" cy="6" r="6" fill="#7a1f2e"/><path d="M3.2 6.2l2 2 3.6-4" fill="none" stroke="#fff" stroke-width="1.4"/></svg>Wedding and trimming services on your gravesite<br>2 times per year: mid-May and mid:September</li>
    <li><svg viewBox="0 0 12 12"><circle cx="6" cy="6" r="6" fill="#7a1f2e"/><path d="M3.2 6.2l2 2 3.6-4" fill="none" stroke="#fff" stroke-width="1.4"/></svg>Monument leveling</li>
    <li><svg viewBox="0 0 12 12"><circle cx="6" cy="6" r="6" fill="#7a1f2e"/><path d="M3.2 6.2l2 2 3.6-4" fill="none" stroke="#fff" stroke-width="1.4"/></svg>Payment ensures grave care forever</li>
  </ul>
  <ul class="features f-3">
    <li><svg viewBox="0 0 12 12"><circle cx="6" cy="6" r="6" fill="#7a1f2e"/><path d="M3.2 6.2l2 2 3.6-4" fill="none" stroke="#fff" stroke-width="1.4"/></svg>Wedding and trimming services on your gravesite approximately every 7 weeks during the growing season: mid-April through mid-October</li>
    <li><svg viewBox="0 0 12 12"><circle cx="6" cy="6" r="6" fill="#7a1f2e"/><path d="M3.2 6.2l2 2 3.6-4" fill="none" stroke="#fff" stroke-width="1.4"/></svg>Monument leveling and cleaning</li>
    <li><svg viewBox="0 0 12 12"><circle cx="6" cy="6" r="6" fill="#7a1f2e"/><path d="M3.2 6.2l2 2 3.6-4" fill="none" stroke="#fff" stroke-width="1.4"/></svg>Payment ensures grave care forever</li>
    <li><svg viewBox="0 0 12 12"><circle cx="6" cy="6" r="6" fill="#7a1f2e"/><path d="M3.2 6.2l2 2 3.6-4" fill="none" stroke="#fff" stroke-width="1.4"/></svg>Full Bed of boxwood shrubs</li>
    <li><svg viewBox="0 0 12 12"><circle cx="6" cy="6" r="6" fill="#7a1f2e"/><path d="M3.2 6.2l2 2 3.6-4" fill="none" stroke="#fff" stroke-width="1.4"/></svg>Replacement of shrubs</li>
    <li><svg viewBox="0 0 12 12"><circle cx="6" cy="6" r="6" fill="#7a1f2e"/><path d="M3.2 6.2l2 2 3.6-4" fill="none" stroke="#fff" stroke-width="1.4"/></svg>Trust certificate</li>
  </ul>

  <div class="price-box pb-1">
    <div class="terms">
      <div class="term"><div class="label">3 Years</div><div class="amount"><sup>$</sup>357</div></div>
      <div class="term"><div class="label">2 Years</div><div class="amount"><sup>$</sup>238</div></div>
      <div class="term"><div class="label">1 Years</div><div class="amount"><sup>$</sup>119</div></div>
    </div>
    <div class="note">Multi year payment locks in current rates<br>Valid through 10/31/2021</div>
  </div>
  <div class="price-box pb-2">
    <div class="pay-label">12 Months Payments of</div>
    <div class="big-amount"><sup>$</sup>255</div>
    <div class="note">Call for single payment discount<br>Valid through 10/31/2021</div>
  </div>
  <div class="price-box pb-3">
    <div class="pay-label">12 Months Payments of</div>
    <div class="big-amount"><sup>$</sup>313</div>
    <div class="note">Call for single payment discount<br>Valid through 10/31/2021</div>
  </div>

  <div class="contact">
    <span style="left:33px">(555) 204-7180</span>
    <div class="sep" style="left:195px"></div>
    <span style="left:227px">48 Orchard Ave. Fairview NJ 07022</span>
    <div class="sep" style="left:555px"></div>
    <span style="left:587px">info@maplecrestgardens.org</span>
  </div>

  <div class="web-band">maplecrestgardens.org</div>
</main>
</body>
</html>
```